Quick Straightforward Billboard Redesign

- Design billboard sized for 10 foot' x 36' foot width live area size and please include bleeds 6" around all sides
- Exact blue color match is imperative in headline, logo, phone number bubble or wherever used. C-83 / M-45 / Y-1 / K-0-
- What I hope to illustrate is that our company offers the best porch screening in the area area, in regards to quality, expertise, durability, storms proof, but we do not build screen porches.
- Current board is attached below from previous designer, and as you can see sizing was off, white space on edges make it appear to be sized incorrectly.
- I also attached my own little mock up idea well well if it helps, favorite image, logo, headline, etc and ideas perhaps on expanding or making this better?

Thanks so much!

Target Market(s)

Drivers and passengers, Southeastern NC, are of immense new construction and high end homes.

Industry/Entity Type

Construction

Colors
0054AA
0677BA
7BADD7
CADEEF
E8F1F8

Requirements
Must have
• Blue color matching
Nice to have
• Design spins or other thoughts on my little mock up

```html
<!DOCTYPE html>
<html lang="en">
<head>
<meta charset="UTF-8">
<title>Porch Screening Billboard</title>
<link href="https://fonts.googleapis.com/css2?family=Anton&family=Poppins:wght@700&display=swap" rel="stylesheet">
<style>
  :root {
    --brand-blue: #0d67b5;
    --brand-green: #2bab55;
    --white: #ffffff;
    --stage: #eef2f6;
    --photo-light: #c9dbe8;
    --photo-warm: #b8ad9c;
  }
  * { margin: 0; padding: 0; box-sizing: border-box; }
  html, body {
    width: 1200px; height: 735px; overflow: hidden;
    background: var(--stage);
  }
  .billboard {
    position: absolute; left: 0; top: 201px;
    width: 1200px; height: 333px;
    background: var(--white);
    overflow: hidden;
  }
  .porch-photo {
    position: absolute; left: 590px; top: 0;
    width: 610px; height: 333px;
    background:
      linear-gradient(90deg, var(--white) 0%, rgba(255,255,255,0.85) 8%, rgba(255,255,255,0) 24%),
      linear-gradient(160deg, var(--photo-light) 0%, var(--photo-warm) 100%);
  }
  .shapes { position: absolute; inset: 0; }
  .headline {
    position: absolute; left: 30px; top: 10px;
    font-family: "Anton", sans-serif;
    font-size: 94px; line-height: 1;
    color: var(--brand-blue);
    letter-spacing: 0.5px;
    white-space: nowrap;
  }
  .tagline {
    position: absolute; left: 31px; top: 116px;
    font-family: "Anton", sans-serif;
    font-size: 68px; line-height: 1;
    color: var(--brand-green);
    white-space: nowrap;
  }
  .company {
    position: absolute; left: 24px; top: 222px;
    display: flex; align-items: center; gap: 12px;
  }
  .company-mark {
    width: 52px; height: 52px;
    background: var(--brand-blue);
  }
  .company-name {
    font-family: "Anton", sans-serif;
    font-size: 27px; line-height: 1.05;
    color: var(--brand-blue);
    text-transform: uppercase;
  }
  .phone {
    position: absolute; left: 445px; top: 265px;
    display: flex; align-items: center; gap: 28px;
  }
  .phone-icon { width: 54px; height: 54px; display: block; }
  .phone-number {
    font-family: "Poppins", sans-serif;
    font-weight: 700;
    font-size: 64px; line-height: 1;
    color: var(--white);
    letter-spacing: 1px;
    white-space: nowrap;
  }
</style>
</head>
<body>
  <main class="billboard">
    <div class="porch-photo" role="img" aria-label="Photo of a screened coastal porch with wicker lounge furniture, ceiling fan and a view over a lawn to a lake"></div>

    <svg class="shapes" width="1200" height="333" viewBox="0 0 1200 333" aria-hidden="true">
      <rect class="base-stripe" x="0" y="313" width="400" height="20" fill="var(--brand-green)"/>
      <polygon class="corner-wedge" points="1016,333 1200,105 1200,333" fill="var(--brand-green)"/>
      <polygon class="phone-band" points="373,333 421,250 1057,250 1016,333" fill="var(--brand-blue)"/>
    </svg>

    <h1 class="headline">Screen Your Porch</h1>
    <p class="tagline">Built For The Coast</p>

    <div class="company">
      <span class="company-mark"></span>
      <span class="company-name">Tidewater<br>Porchworks</span>
    </div>

    <div class="phone">
      <svg class="phone-icon" viewBox="0 0 54 54" aria-hidden="true">
        <circle cx="27" cy="27" r="27" fill="var(--white)"/>
        <path d="M19.5 14.5c1-.8 2.3-.6 3 .4l2.6 3.8c.6.9.5 2.1-.3 2.8l-1.7 1.5c1.2 3 3.5 5.5 6.3 7l1.6-1.6c.8-.7 2-.8 2.8-.2l3.8 2.6c1 .7 1.2 2.1.4 3l-2.1 2.4c-1 1.1-2.600 1.5-4 1-8-2.9-13.5-8.7-16-16.5-.4-1.4 0-2.9 1.1-3.8z" fill="var(--brand-blue)"/>
        <path d="M29 16a9 9 0 0 1 9 9M29 11.5a13.5 13.5 0 0 1 13.5 13.5" fill="none" stroke="var(--brand-blue)" stroke-width="2.4" stroke-linecap="round"/>
      </svg>
      <span class="phone-number">910-555-0142</span>
    </div>
  </main>
</body>
</html>
```